Fantastic Banners Needed Total 24

I need 4 campaigns to have banners made, 6 banner sizes each so 24 total banners. Here are the landing pages with the messaging.

http://www.nearbyshopratings.example/The-Crafton-Colleges-66323.html

http://www.nearbyshopratings.example/Halvern-University-66322.html

http://www.nearbyshopratings.example/The-Brightwell-School-of-Sound-and-Screen-Media-66321.html

http://www.nearbyshopratings.example/Clearpath-Debt-66320.html

Need to get done asap. Much more work can be following right after. Here are the sizes

Sorry fix a typo. These sizes:

300 X 50
300x250
320 X50
216 X36
168 X 28
120 X 20

Radio

Must have
• Phone number in ad call to action

```html
<!DOCTYPE html>
<html lang="en">
<head>
<meta charset="utf-8">
<title>Brightwell School – Radio Banner Set</title>
<link rel="stylesheet" href="https://fonts.googleapis.com/css2?family=Arimo:wght@400;700&display=swap">
<style>
  :root {
    --page: #ffffff;
    --ink-black: #0b0b0c;
    --panel-dark: #1a2433;
    --panel-mid: #2c3a4f;
    --panel-light: #3d4e66;
    --text-white: #ffffff;
    --accent-green: #a6e01c;
    --cta-light: #d8f65a;
    --cta-dark: #8fcf12;
    --cta-ink: #121212;
    --photo-warm: #c9796a;
    --photo-red: #d8352a;
    --photo-dark: #3a2a2a;
    --frame-white: #f4f4f4;
  }
  * { box-sizing: border-box; margin: 0; padding: 0; }
  html, body {
    width: 1044px; height: 1200px; overflow: hidden;
    background: var(--page);
    font-family: "Arimo", Arial, sans-serif;
  }
  .canvas { position: relative; width: 1044px; height: 1200px; }

  /* ---------- shared banner ---------- */
  .banner {
    position: absolute; overflow: hidden;
    background: linear-gradient(180deg, var(--panel-light) 0%, var(--panel-mid) 45%, var(--panel-dark) 100%);
    color: var(--text-white);
  }
  .brand {
    position: absolute; left: 0; top: 0; bottom: 0; width: 32%;
    background: var(--ink-black);
    display: flex; align-items: center; justify-content: center;
  }
  .brand-name {
    font-weight: 700; font-size: 2.3em; letter-spacing: -0.01em;
    color: var(--text-white); white-space: nowrap;
  }
  .headline {
    position: absolute; left: 32%; width: 38%; top: 14%;
    text-align: center; font-weight: 700; font-size: 1.95em; line-height: 1.3;
    white-space: nowrap;
  }
  .headline em { font-style: normal; color: var(--accent-green); }
  .photo-frame {
    position: absolute; top: 0; bottom: 0; left: 68%; right: 0;
    background: var(--frame-white);
    clip-path: polygon(22% 0, 100% 0, 100% 100%, 0 100%);
  }
  .photo {
    position: absolute; top: 0; bottom: 0; left: 71%; right: 0;
    background: radial-gradient(circle at 60% 40%, var(--photo-warm) 0%, var(--photo-red) 35%, var(--photo-dark) 80%);
    clip-path: polygon(22% 0, 100% 0, 100% 100%, 0 100%);
  }
  .cta {
    position: absolute; left: 70%; right: 1.5%; top: 58%; bottom: 8%;
    background: linear-gradient(180deg, var(--cta-light) 0%, var(--cta-dark) 100%);
    border: 0.12em solid var(--text-white);
    color: var(--cta-ink); font-weight: 700; font-size: 1.8em;
    display: flex; align-items: center; justify-content: center; white-space: nowrap;
  }

  /* ---------- strip sizes ---------- */
  .size-120x20 { left: 430px; top: 110px; width: 240px; height: 40px; font-size: 4px; }
  .size-168x28 { left: 380px; top: 178px; width: 336px; height: 56px; font-size: 5.6px; }
  .size-216x36 { left: 332px; top: 252px; width: 432px; height: 72px; font-size: 7.2px; }
  .size-300x50 { left: 248px; top: 354px; width: 600px; height: 104px; font-size: 10px; }
  .size-320x50 { left: 228px; top: 482px; width: 640px; height: 100px; font-size: 10px; }

  /* ---------- square 300x250 ---------- */
  .size-300x250 {
    left: 248px; top: 604px; width: 600px; height: 500px; font-size: 10px;
    background: linear-gradient(180deg, var(--ink-black) 0%, var(--panel-dark) 35%, var(--panel-mid) 70%, var(--panel-dark) 100%);
  }
  .size-300x250 .brand {
    top: 11%; bottom: auto; height: 22%; width: 54%;
    justify-content: flex-start; padding-left: 1.6em;
  }
  .size-300x250 .brand-name { font-size: 4.2em; }
  .size-300x250 .photo-frame { left: 40%; bottom: 52%; clip-path: polygon(12% 0, 100% 0, 100% 100%, 50% 100%, 38% 60%); }
  .size-300x250 .photo { left: 44%; bottom: 54%; clip-path: polygon(10% 0, 100% 0, 100% 100%, 52% 100%, 38% 62%); }
  .size-300x250 .headline {
    left: 0; width: 100%; top: 58%; font-size: 4.6em; line-height: 1.25;
  }
  .size-300x250 .cta {
    left: 19%; right: 18%; top: 82%; bottom: 5%;
    font-size: 4.4em; border-width: 0.06em; border-radius: 0.15em;
  }
</style>
</head>
<body>
<div class="canvas">

  <div class="banner size-120x20">
    <div class="brand"><span class="brand-name">Brightwell</span></div>
    <p class="headline">Make the <em>Career</em> change<br>that can change your <em>life</em></p>
    <div class="photo-frame"></div>
    <div class="photo" role="img" aria-label="Photo of a smiling radio host in headphones at a studio microphone"></div>
    <div class="cta">(888) 555-0147</div>
  </div>

  <div class="banner size-168x28">
    <div class="brand"><span class="brand-name">Brightwell</span></div>
    <p class="headline">Make the <em>Career</em> change<br>that can change your <em>life</em></p>
    <div class="photo-frame"></div>
    <div class="photo" role="img" aria-label="Photo of a smiling radio host in headphones at a studio microphone"></div>
    <div class="cta">(888) 555-0147</div>
  </div>

  <div class="banner size-216x36">
    <div class="brand"><span class="brand-name">Brightwell</span></div>
    <p class="headline">Make the <em>Career</em> change<br>that can change your <em>life</em></p>
    <div class="photo-frame"></div>
    <div class="photo" role="img" aria-label="Photo of a smiling radio host in headphones at a studio microphone"></div>
    <div class="cta">(888) 555-0147</div>
  </div>

  <div class="banner size-300x50">
    <div class="brand"><span class="brand-name">Brightwell</span></div>
    <p class="headline">Make the <em>Career</em> change<br>that can change your <em>life</em></p>
    <div class="photo-frame"></div>
    <div class="photo" role="img" aria-label="Photo of a smiling radio host in headphones at a studio microphone"></div>
    <div class="cta">(888) 555-0147</div>
  </div>

  <div class="banner size-320x50">
    <div class="brand"><span class="brand-name">Brightwell</span></div>
    <p class="headline">Make the <em>Career</em> change<br>that can change your <em>life</em></p>
    <div class="photo-frame"></div>
    <div class="photo" role="img" aria-label="Photo of a smiling radio host in headphones at a studio microphone"></div>
    <div class="cta">(888) 555-0147</div>
  </div>

  <div class="banner size-300x250">
    <div class="photo-frame"></div>
    <div class="photo" role="img" aria-label="Photo of a smiling radio host in headphones at a studio microphone"></div>
    <div class="brand"><span class="brand-name">Brightwell</span></div>
    <p class="headline">Make the <em>Career</em> change<br>that can change your <em>life</em></p>
    <div class="cta">(888) 555-0147</div>
  </div>

</div>
</body>
</html>
```